Book cover for book about ex-wifes

I need a book cover for my new book called "Tidligere brude fra Solen, Stormen og Lindevang" - In english: "Former brides from Sun, Storm and Lindevang" (Hørsholm is a posh city in Denmark).

The book is by men for men about ex-wifes and about how to avoid getting them.
Is it a book from a sexologist and couples therapist to men on how to improve relations.

Men (and curious women)

• Something that indicate three types of ex-wifes

And the author name “Jonas Beltoft”
• Something that says something about relationships, couples and how to stay together (or how to avoid not breaking up)
• No hate

```html
<!DOCTYPE html>
<html lang="da">
<head>
<meta charset="utf-8">
<title>Tidligere brude fra Solen, Stormen og Lindevang – Jonas Beltoft</title>
<link rel="stylesheet" href="https://fonts.googleapis.com/css2?family=Figtree:ital,wght@0,300;0,700;1,300&display=swap">
<style>
  :root {
    --red: #ff0a33;
    --magenta: #ff06cc;
    --hot-pink: #ff0a8c;
    --ink: #ffffff;
  }
  * { margin: 0; padding: 0; box-sizing: border-box; }
  html, body {
    width: 846px;
    height: 1200px;
    overflow: hidden;
    background: var(--red);
  }
  .cover {
    position: relative;
    width: 846px;
    height: 1200px;
    overflow: hidden;
    font-family: "Figtree", "Avenir Next", sans-serif;
    color: var(--ink);
  }
  .cover-photo {
    position: absolute;
    inset: 0;
    background:
      radial-gradient(ellipse 210px 170px at 190px 80px, var(--magenta) 0%, transparent 70%),
      radial-gradient(ellipse 260px 330px at 400px 460px, var(--magenta) 0%, var(--magenta) 55%, transparent 80%),
      radial-gradient(ellipse 140px 90px at 390px 660px, var(--hot-pink) 0%, transparent 80%),
      radial-gradient(ellipse 250px 190px at 390px 820px, var(--magenta) 0%, transparent 75%),
      radial-gradient(ellipse 150px 110px at 440px 960px, var(--magenta) 0%, transparent 80%),
      radial-gradient(ellipse 170px 260px at 740px 600px, var(--hot-pink) 0%, transparent 80%),
      radial-gradient(ellipse 200px 240px at 60px 980px, var(--hot-pink) 0%, transparent 80%),
      var(--red);
  }
  .cover-text {
    position: absolute;
    left: 136px;
    top: 0;
  }
  .title {
    position: absolute;
    top: 236px;
    left: 0;
    font-weight: 700;
    font-size: 78px;
    line-height: 87px;
    letter-spacing: -0.5px;
    white-space: nowrap;
  }
  .title span { display: block; }
  .author {
    position: absolute;
    top: 622px;
    left: 0;
    font-weight: 300;
    font-size: 50px;
    line-height: 60px;
    white-space: nowrap;
  }
  .epigraph {
    position: absolute;
    top: 954px;
    left: 0;
    font-style: italic;
    font-weight: 300;
    white-space: nowrap;
  }
  .epigraph-quote {
    font-size: 28px;
    line-height: 35px;
  }
  .epigraph-quote span { display: block; }
  .epigraph-source {
    display: inline-block;
    margin-top: 14px;
    font-size: 19px;
    line-height: 22px;
    text-transform: uppercase;
    text-decoration: underline;
    text-underline-offset: 4px;
    text-decoration-thickness: 1px;
  }
</style>
</head>
<body>
  <main class="cover">
    <div class="cover-photo" role="img" aria-label="Blurred photo in red and magenta tones of a couple sharing cups of coffee"></div>
    <div class="cover-text">
      <h1 class="title">
        <span>Tidligere brude</span>
        <span>fra Solen,</span>
        <span>Stormen og</span>
        <span>Lindevang</span>
      </h1>
      <p class="author">Jonas Beltoft</p>
      <figure class="epigraph">
        <blockquote class="epigraph-quote">
          <span>“There is no remedy</span>
          <span>for love but to love more”</span>
        </blockquote>
        <figcaption class="epigraph-source">Marguerite Delval</figcaption>
      </figure>
    </div>
  </main>
</body>
</html>
```